A Freight forwarding (transportation/shipping) company requires stationary designs

We need The following:
1. Letterhead
2. Letter Envelope
3. Business Card Design
4. A4 Paper Envelope
5. A4 Paper Folder (One that is 2xA4 foldable size which we can open in half and we can put a paper in between and has a lot for business card)
6. A5 Paper (To be used for notes taking)
a design for a freight forwarding company named KORVALE DIMAS INTERNATIONAL TRANSPORTATION.
(We are active in Sea Transportation, Truck transportation, and Air Transportation, (printed design in PDF is required with all open source files for editing - lamination accepted)
Playing around with the Logo is accepted,, Korvale Logo.png is the correct logo.
Example of folder, envelopes, and notepad attached
Address of the company is :
No 7, 4th Tarvandi Gharbi, Nasim Dareh Blvd,
Mashhad, IR
Tel : +98 51 30000000
Fax : +98 51 30000001
Website : www.korvale-example.com
Email : info@korvale-example.com

```html
<!DOCTYPE html>
<html lang="en">
<head>
<meta charset="utf-8">
<title>Korvale Dimas Letterhead</title>
<link rel="stylesheet" href="https://fonts.googleapis.com/css2?family=Arimo:wght@400;700&display=swap">
<style>
  :root {
    --backdrop: #e4e4e4;
    --paper: #ffffff;
    --ink: #2a2a2a;
    --brand-blue: #3a3e8c;
    --brand-green: #2f8f3f;
  }
  * { box-sizing: border-box; margin: 0; padding: 0; }
  html, body {
    width: 1200px; height: 907px; overflow: hidden;
    background: var(--backdrop);
    font-family: "Arimo", Arial, sans-serif;
    color: var(--ink);
  }
  .letterhead {
    position: absolute; left: 296px; top: 24px;
    width: 608px; height: 860px;
    background: var(--paper);
    box-shadow: 0 4px 18px rgba(0,0,0,.18);
    overflow: hidden;
  }
  .brand {
    position: absolute; right: 48px; top: 38px;
    display: flex; flex-direction: column; align-items: center; gap: 6px;
    color: var(--brand-blue);
  }
  .brand-mark {
    width: 58px; height: 58px; border-radius: 50%;
    border: 5px solid var(--brand-blue);
  }
  .brand-name { font-size: 13px; font-weight: 700; letter-spacing: .5px; }
  .brand-tagline { font-size: 13px; font-weight: 700; margin-top: -6px; transform: scale(.55); transform-origin: top center; }
  .recipient {
    position: absolute; left: 64px; top: 150px;
    font-size: 10.5px; line-height: 13px; font-style: normal;
  }
  .recipient strong { font-weight: 700; }
  .letter-body {
    position: absolute; left: 64px; top: 228px; width: 480px;
    font-size: 10.5px; line-height: 13px;
  }
  .letter-body p { margin-bottom: 11px; }
  .signature {
    position: absolute; left: 64px; top: 500px;
    font-size: 10.5px; line-height: 13px;
  }
  .signature strong { font-weight: 700; }
  .footer-band {
    position: absolute; left: 0; right: 0; bottom: 0; height: 150px;
    background: linear-gradient(180deg, var(--brand-blue) 0%, var(--brand-blue) 70%, var(--brand-green) 100%);
  }
  .contact {
    position: absolute; right: 40px; top: 600px;
    font-size: 8px; line-height: 12px; list-style: none;
  }
  .contact li { display: flex; align-items: center; gap: 5px; }
  .contact .icon { width: 8px; height: 8px; flex: none; }
</style>
</head>
<body>
  <main class="letterhead">
    <header class="brand">
      <span class="brand-mark"></span>
      <span class="brand-name">KORVALE DIMAS</span>
      <span class="brand-tagline">International Transportation</span>
    </header>

    <address class="recipient">
      <strong>Mr. Daniel Reeve</strong><br>
      Managing Director<br>
      Westbrook Holdings<br>
      200 W Oak Avenue
    </address>

    <section class="letter-body">
      <p>Lorem ipsum dolor sit amet, consectetuer adipiscing elit. Nam cursus. Morbi ut mi. Nullam enim leo, egestas id, condimentum at, laoreet mattis, massa. Sed eleifend nonummy diam. Praesent mauris ante, elementum et, bibendum at, posuere sit amet, nibh. Duis tincidunt lectus quis dui viverra vestibulum.</p>
      <p>Suspendisse vulputate aliquam dui. Nulla elementum dui ut augue. Aliquam vehicula mi at mauris. Maecenas placerat, nisl at consequat rhoncus, sem nunc gravida justo, quis eleifend arcu velit quis lacus. Morbi magna magna, tincidunt a, mattis non, imperdiet vitae, tellus. Sed odio est, auctor ac, sollicitudin in, consequat vitae, orci. Fusce id felis. Vivamus sollicitudin.</p>
      <p>Metus eget eros. Pellentesque habitant morbi tristique senectus et netus et malesuada fames ac turpis egestas. In posuere felis nec tortor. Pellentesque faucibus. Ut accumsan ultricies elit. Maecenas at justo id velit placerat molestie. Donec dictum lectus non odio. Cras a ante vitae enim iaculis aliquam.</p>
      <p>Mauris nunc quam, venenatis nec, euismod sit amet, egestas placerat, est. Pellentesque habitant morbi tristique senectus et netus et malesuada fames ac turpis egestas. Cras id elit. Integer quis urna. Ut ante enim, dapibus malesuada, fringilla eu, condimentum quis, tellus. Aenean porttitor eros vel dolor. Donec convallis pede venenatis nibh. Duis quam. Nam eget.</p>
      <p>Thank you for being one of our valued customers.</p>
    </section>

    <div class="signature">
      <strong>Name Here</strong><br>
      CEO
    </div>

    <ul class="contact">
      <li>No 7, 4th Tarvandi Gharbi,</li>
      <li>Nasim Dareh Blvd, Mashhad, IR</li>
      <li>+98 51 30000000
        <svg class="icon" viewBox="0 0 8 8" aria-hidden="true"><circle cx="4" cy="4" r="4" fill="var(--brand-blue)"/><path d="M2.6,2 L3.4,2 L3.6,3 L3.1,3.4 Q3.6,4.5 4.6,4.9 L5,4.4 L6,4.6 L6,5.4 Q3,5.6 2.6,2 Z" fill="#fff"/></svg></li>
      <li>+98 51 30000001
        <svg class="icon" viewBox="0 0 8 8" aria-hidden="true"><circle cx="4" cy="4" r="4" fill="var(--brand-blue)"/><rect x="2.2" y="2.6" width="3.6" height="2.8" fill="#fff"/></svg></li>
      <li>info@korvale-example.com
        <svg class="icon" viewBox="0 0 8 8" aria-hidden="true"><circle cx="4" cy="4" r="4" fill="var(--brand-blue)"/><path d="M2,2.8 H6 V5.2 H2 Z M2,2.8 L4,4.2 L6,2.8" fill="none" stroke="#fff" stroke-width=".6"/></svg></li>
      <li>www.korvale-example.com
        <svg class="icon" viewBox="0 0 8 8" aria-hidden="true"><circle cx="4" cy="4" r="4" fill="var(--brand-blue)"/><circle cx="4" cy="4" r="2" fill="none" stroke="#fff" stroke-width=".6"/></svg></li>
    </ul>

    <div class="footer-band" role="img" aria-label="Decorative footer wave in brand blue with a green accent stripe"></div>
  </main>
</body>
</html>
```